Doctor in Veterinary Medecine/ veterinarian

I am a vet and would like a buisness card which is simple yet elegant and professional.
My aim is to help as much animals as I can. My main field of expertise are dogs and cats. I would like the card to reflect a "family doctor" feeling.
It should not be the traditional picture of a paw or a dog but yet it should have a sign of a pet on it. I would like to have my name Lina Haddoul as well as my profession D.V.M and my number.

Target Market(s)

Lebanese population who have pets

Industry/Entity Type

Doctor

Contact Information for Business Card

Should contain my profession " D.V.M", my full name "Lina Haddoul" and my number "0096171539214"

Requirements
Must have
• A certain picture depicting my profession
Nice to have
• Some sort of picture related to pets and animals
Should not have
• A picture of a paw or a dog. I need something more creative

```html
<!DOCTYPE html>
<html lang="en">
<head>
<meta charset="utf-8">
<title>Lina Haddoul, D.V.M – Business Card</title>
<link href="https://fonts.googleapis.com/css2?family=Arimo:wght@700&display=swap" rel="stylesheet">
<style>
  :root {
    --backdrop: #0f3d55;
    --card-white: #ffffff;
    --panel-grey: #d9d9d8;
    --brand-blue: #2b9fd3;
    --brand-blue-soft: rgba(43, 159, 211, 0.55);
    --brand-blue-fade: rgba(43, 159, 211, 0);
    --phone-blue: #1a7fb5;
    --ink: #000000;
  }
  html, body {
    margin: 0;
    width: 1200px;
    height: 1200px;
    overflow: hidden;
    background: var(--backdrop);
  }
  .card {
    position: absolute;
    left: 50px;
    top: 285px;
    width: 1100px;
    height: 630px;
    background: var(--card-white);
    box-shadow: 6px -6px 0 var(--ink);
    overflow: hidden;
    font-family: "Arimo", Arial, sans-serif;
  }
  .card-shapes {
    position: absolute;
    inset: 0;
  }
  .pet-illustration {
    position: absolute;
    left: 200px;
    top: 165px;
    width: 285px;
    height: 215px;
    background: radial-gradient(ellipse at 55% 55%, var(--brand-blue-soft) 0%, var(--brand-blue-fade) 72%);
  }
  .profession {
    position: absolute;
    left: 180px;
    top: 385px;
    margin: 0;
    font-size: 112px;
    font-weight: 700;
    letter-spacing: 2px;
    line-height: 1;
    color: var(--brand-blue);
  }
  .paw-mark {
    position: absolute;
    left: 790px;
    top: 80px;
    width: 180px;
    height: 180px;
    background: radial-gradient(circle at 50% 55%, var(--brand-blue-soft) 0%, var(--brand-blue-fade) 70%);
  }
  .contact {
    position: absolute;
    left: 700px;
    top: 285px;
    width: 380px;
    text-align: center;
  }
  .contact-name {
    margin: 0;
    font-size: 60px;
    font-weight: 700;
    line-height: 1.1;
    color: var(--ink);
  }
  .contact-phone {
    margin: 4px 0 0;
    font-size: 44px;
    font-weight: 700;
    line-height: 1.1;
    color: var(--phone-blue);
  }
</style>
</head>
<body>
  <div class="card">
    <svg class="card-shapes" viewBox="0 0 1100 630" width="1100" height="630" aria-hidden="true">
      <polygon points="0,0 550,0 600,440 190,630 0,160" fill="var(--panel-grey)"/>
      <polygon points="1100,440 1100,630 600,630" fill="var(--brand-blue)"/>
    </svg>
    <div class="pet-illustration" role="img" aria-label="Silhouette of a dog, cat and rabbit standing together"></div>
    <p class="profession">D.V.M</p>
    <div class="paw-mark" role="img" aria-label="Paw print icon"></div>
    <div class="contact">
      <p class="contact-name">Lina Haddoul</p>
      <p class="contact-phone">0096171539214</p>
    </div>
  </div>
</body>
</html>
```